Torvane PT Business Card

I need the card to be bright/bold colours to stand out amongst others.
It needs to have my company logo.
I was not interested in pictures etc just a layout that attracts attention.

I have attached my old design which is very plain. I also needed change the contact details. And my description changed to Personal Trainer
Phone 0427391058
Facebook Torvane PT
No email address please, no street address.
And only Torvane PT (Please remove anything to do with Torvane Supplements)

```html
<!DOCTYPE html>
<html lang="en">
<head>
<meta charset="utf-8">
<title>Torvane PT Business Card</title>
<link href="https://fonts.googleapis.com/css2?family=Open+Sans:wght@400;600;700;800&display=swap" rel="stylesheet">
<style>
  :root {
    --page-bg: #e9e7e3;
    --gold-light: #f6cf3a;
    --gold-mid: #f0b51e;
    --gold-deep: #e49a12;
    --brand-blue: #1d4f91;
    --band-blue: #1a4a8c;
    --accent-gold: #f2b81f;
    --text-dark: #3a3326;
  }
  * { margin: 0; padding: 0; box-sizing: border-box; }
  html, body { width: 1200px; height: 969px; overflow: hidden; }
  body {
    background: var(--page-bg);
    font-family: "Open Sans", Arial, sans-serif;
    position: relative;
  }
  .business-card {
    position: absolute;
    left: 100px;
    top: 201px;
    width: 1000px;
    height: 567px;
    border-radius: 28px;
    overflow: hidden;
    background: linear-gradient(160deg, var(--gold-light) 0%, var(--gold-mid) 45%, var(--gold-deep) 100%);
    box-shadow: 0 18px 40px rgba(0,0,0,0.18);
  }
  .card-shapes { position: absolute; inset: 0; }
  .contact-block {
    position: absolute;
    left: 38px;
    top: 145px;
    color: var(--text-dark);
  }
  .person-name {
    font-size: 35px;
    font-weight: 700;
    color: var(--brand-blue);
    letter-spacing: 0.5px;
    line-height: 1.1;
  }
  .person-role {
    font-size: 27px;
    margin-top: 8px;
  }
  .contact-list { list-style: none; margin-top: 110px; }
  .contact-list li {
    display: flex;
    align-items: center;
    font-size: 27px;
    line-height: 39px;
  }
  .contact-icon { width: 24px; height: 24px; margin-right: 14px; flex: none; }
  .social-square {
    width: 22px; height: 22px; margin-right: 16px; flex: none;
    background: var(--brand-blue); border-radius: 3px;
  }
  .brand-name {
    position: absolute;
    left: 540px;
    top: 240px;
    width: 410px;
    text-align: center;
    white-space: nowrap;
    font-size: 56px;
    line-height: 70px;
    font-weight: 800;
    color: var(--brand-blue);
    letter-spacing: 1px;
  }
</style>
</head>
<body>
  <section class="business-card">
    <svg class="card-shapes" width="1000" height="567" viewBox="0 0 1000 567">
      <defs>
        <linearGradient id="frostFill" x1="0" y1="0" x2="1" y2="1">
          <stop offset="0" stop-color="#fafbfc"/>
          <stop offset="1" stop-color="#e6e9ed"/>
        </linearGradient>
      </defs>
      <path class="blue-band" d="M 790 0 C 520 50 405 190 420 300 C 435 420 560 510 700 567 L 1000 567 L 1000 0 Z" fill="var(--band-blue)"/>
      <path class="gold-stripe" d="M 850 0 C 580 55 458 195 470 300 C 482 410 600 505 760 567 L 1000 567 L 1000 0 Z" fill="var(--accent-gold)"/>
      <path class="inner-band" d="M 862 0 C 595 58 470 198 482 300 C 494 408 612 505 775 567 L 1000 567 L 1000 0 Z" fill="var(--band-blue)"/>
      <path class="frost-panel" d="M 905 0 C 650 60 520 200 532 300 C 544 410 665 505 835 567 L 1000 567 L 1000 0 Z" fill="url(#frostFill)"/>
    </svg>

    <div class="contact-block">
      <h1 class="person-name">DANE MERCER</h1>
      <p class="person-role">Personal Trainer</p>
      <ul class="contact-list">
        <li>
          <svg class="contact-icon" viewBox="0 0 24 24" aria-hidden="true">
            <path d="M6.6 10.8a15.1 15.1 0 0 0 6.6 6.6l2.2-2.2a1 1 0 0 1 1-.25 11.4 11.4 0 0 0 3.6.57 1 1 0 0 1 1 1V20a1 1 0 0 1-1 1A17 17 0 0 1 3 4a1 1 0 0 1 1-1h3.5a1 1 0 0 1 1 1c0 1.25.2 2.45.57 3.57a1 1 0 0 1-.25 1z" fill="var(--brand-blue)"/>
          </svg>
          0427391058
        </li>
        <li><span class="social-square"></span>Torvane PT</li>
      </ul>
    </div>

    <div class="brand-name">TORVANE PT</div>
  </section>
</body>
</html>
```